Two Day Training Event includes a Dinner/Bowling Party at Pinhollow in Troy, MI

I would like a postcard to attract Insurance Agents to an KRV meeting calling it a summit or something like that. Just something to mail to insurance agents telling them about our upcoming event with over 20 carriers. An opportunity to certify face to face with MAPD carriers and see what 2020 has to offer. Prior to OEP OPen Enrollment and AEP Annual Election period we have a number of meetings. Carriers want to come especially if we can get a number of agents. We are going to go to Pinhollow a fun bowling alley for dinner, drinks and bowling to network and talk about the upcoming year.

Target Market(s)

Existing and new insurance agents

Industry/Entity Type

Insurance Broker

Contact Information for Business Card

Looking for a new card design I sent my LOGO and can upload my existing card.

Font styles to use
Serif

Colors

Designer to choose colors to be used in the design.

Requirements
Must have
• Dates Sept 16 and 17th
• location Larkfield Conference Hall in Troy MI
• times
Nice to have
• It would be nice to see a fun design.

```html
<!DOCTYPE html>
<html lang="en">
<head>
<meta charset="utf-8">
<title>The Year Ahead Summit – Postcard</title>
<link href="https://fonts.googleapis.com/css2?family=Roboto:wght@400;700;900&family=Roboto+Condensed:ital,wght@0,400;0,700;1,700&family=Oswald:wght@600&family=Dancing+Script:wght@700&display=swap" rel="stylesheet">
<style>
  :root {
    --backdrop: #e9ddc6;
    --red: #e8141b;
    --blue: #1a27c9;
    --navy: #1b2a8f;
    --yellow: #ffe21a;
    --white: #ffffff;
    --ink: #1a1a1a;
    --orange-light: #f3c15a;
    --orange-deep: #c9731c;
    --grey: #9a9a9a;
  }
  * { box-sizing: border-box; margin: 0; padding: 0; }
  html, body { width: 1200px; height: 429px; overflow: hidden; background: var(--backdrop); }
  body { position: relative; font-family: "Roboto", Arial, sans-serif; }

  .postcard { position: absolute; top: 28px; width: 535px; height: 364px; overflow: hidden; }
  .postcard--front { left: 48px; background: var(--orange-light); }
  .postcard--back { left: 620px; background: var(--white); box-shadow: 0 1px 3px rgba(0,0,0,.15); }

  /* Front */
  .front-photo { position: absolute; inset: 0;
    background: radial-gradient(ellipse at 70% 55%, #7c6a68 0%, #a48a6a 35%, transparent 60%),
                linear-gradient(160deg, #f6d27a 0%, #e9a646 55%, #c9731c 100%); }
  .front-header { position: absolute; left: 0; top: 0; width: 535px; height: 160px; }
  .front-title { position: absolute; left: 46px; top: 14px; color: var(--white);
    font: 700 25px/1 "Roboto", sans-serif; }
  .front-subtitle { position: absolute; left: 46px; top: 48px; color: var(--yellow);
    font: 700 16px/22px "Roboto", sans-serif; }
  .front-teaser { position: absolute; left: 384px; top: 10px; color: var(--white);
    font: italic 700 16px/22px "Roboto Condensed", sans-serif; }

  .event-info { position: absolute; left: 22px; top: 148px; width: 170px; text-align: center; }
  .event-dates { color: var(--white); font: 600 15px/1 "Oswald", sans-serif; letter-spacing: .3px; }
  .event-venue { margin-top: 8px; color: var(--navy); font: 700 14px/17px "Roboto Condensed", sans-serif; }
  .enjoy { position: absolute; left: 44px; top: 219px; color: var(--red);
    font: 700 17px/1 "Dancing Script", cursive; }
  .perks { position: absolute; left: 36px; top: 244px; list-style: none; }
  .perks li { display: flex; align-items: center; gap: 9px; color: var(--white);
    font: 700 14px/20px "Roboto", sans-serif; letter-spacing: .5px; }
  .perks li::before { content: ""; width: 9px; height: 9px; border-radius: 50%; background: var(--white); }
  .venue-tag { position: absolute; left: 35px; top: 314px; display: flex; align-items: center; gap: 6px; }
  .venue-tag__at { width: 26px; height: 26px; border-radius: 50%; background: var(--blue); color: var(--white);
    font: 700 13px/26px "Roboto", sans-serif; text-align: center; }
  .venue-tag__name { color: var(--white); font: 900 17px/1 "Roboto", sans-serif; }

  .snack-art { position: absolute; left: 150px; top: 255px; width: 150px; height: 60px; border-radius: 30px;
    background: radial-gradient(ellipse, #a83a14 0%, #c96a2a 55%, transparent 75%); }

  .rsvp-box { position: absolute; left: 182px; top: 298px; width: 342px; height: 51px; border-radius: 8px;
    background: rgba(255,255,255,.88); }
  .rsvp-box__label { position: absolute; left: 14px; top: 8px; color: var(--blue);
    font: 700 10px/1 "Roboto Condensed", sans-serif; }
  .rsvp-box__phone { position: absolute; left: 14px; top: 22px; color: var(--red); display: flex; align-items: center; gap: 4px;
    font: 700 15px/1 "Roboto", sans-serif; }
  .brand-name { color: var(--blue); font: 900 30px/1 "Roboto", sans-serif; }
  .rsvp-box .brand-name { position: absolute; left: 226px; top: 10px; }

  /* Back */
  .about { position: absolute; left: 35px; top: 14px; width: 210px; }
  .about__title { color: var(--blue); font: 700 12px/1 "Roboto", sans-serif; margin-bottom: 6px; }
  .about__text { color: var(--ink); font: 400 8px/13px "Roboto Condensed", sans-serif; }
  .back .brand-name { }
  .back-brand { position: absolute; left: 342px; top: 20px; }
  .mail-address { position: absolute; left: 358px; top: 58px; color: var(--ink);
    font: 400 8px/11px "Roboto Condensed", sans-serif; }
  .stamp-box { position: absolute; left: 472px; top: 17px; width: 57px; height: 63px; border: 2px solid var(--grey); }
  .back-title { position: absolute; left: 32px; top: 126px; color: var(--blue); font: 700 17px/1 "Roboto", sans-serif; }
  .back-teaser { position: absolute; left: 30px; top: 151px; color: var(--red); font: italic 700 14px/1 "Roboto Condensed", sans-serif; }
  .back-band { position: absolute; left: 0; top: 172px; width: 268px; height: 36px; background: var(--blue);
    color: var(--white); text-align: center; font: 700 11px/16px "Roboto Condensed", sans-serif; padding-top: 2px; }
  .family-photo { position: absolute; left: 150px; top: 200px; width: 300px; height: 164px;
    background: radial-gradient(ellipse at 55% 55%, #e7d2be 0%, #eee3d8 40%, rgba(255,255,255,0) 72%); }
  .back-contact { position: absolute; left: 70px; top: 218px; }
  .back-contact__label { color: var(--blue); font: 700 10px/1 "Roboto Condensed", sans-serif; }
  .back-contact__phone { margin-top: 4px; color: var(--red); display: flex; align-items: center; gap: 4px;
    font: 700 13px/1 "Roboto", sans-serif; }
  .back-contact__list { list-style: none; margin-top: 6px; margin-left: -4px; }
  .back-contact__list li { display: flex; align-items: center; gap: 5px; color: var(--ink);
    font: 400 9px/13px "Roboto", sans-serif; }
  .icon { flex: none; }
</style>
</head>
<body>

<section class="postcard postcard--front" aria-label="Postcard front">
  <div class="front-photo" role="img" aria-label="Photo of friends bowling together in a bright bowling alley"></div>

  <svg class="front-header" viewBox="0 0 535 160" aria-hidden="true">
    <path d="M0 0H535V78C400 84 230 88 0 134Z" fill="var(--red)"/>
    <path d="M0 134C230 88 400 84 535 78V84C400 92 230 96 0 142Z" fill="var(--blue)"/>
  </svg>

  <h1 class="front-title">The Year Ahead Summit</h1>
  <p class="front-subtitle">An opportunity to certify face to face<br>with over 20 MAPD carriers</p>
  <p class="front-teaser">Find out what<br>2020 has to offer</p>

  <div class="event-info">
    <p class="event-dates">SEPT 16TH AND 17TH</p>
    <p class="event-venue">Larkfield<br>Conference Hall<br>Troy, MI</p>
  </div>
  <p class="enjoy">Enjoy</p>
  <ul class="perks">
    <li>DINNER</li>
    <li>DRINKS</li>
    <li>BOWLING</li>
  </ul>
  <div class="venue-tag">
    <span class="venue-tag__at">at</span>
    <span class="venue-tag__name">Pinhollow</span>
  </div>

  <div class="snack-art" role="img" aria-label="Platter of wings with colourful cocktails"></div>

  <div class="rsvp-box">
    <p class="rsvp-box__label">CONFIRM YOUR ATTENDANCE</p>
    <p class="rsvp-box__phone">
      <svg class="icon" width="13" height="13" viewBox="0 0 16 16" aria-hidden="true"><circle cx="8" cy="8" r="7" fill="none" stroke="currentColor" stroke-width="1.4"/><path d="M5 4.5l1.5-.5 1 2-1 .8c.4 1 1 1.6 1.9 2l.8-1 2 1-.5 1.5c-2.8.2-5.6-2.7-5.7-5.8z" fill="currentColor"/></svg>
      (800) 555-0142
    </p>
    <span class="brand-name">KRV</span>
  </div>
</section>

<section class="postcard postcard--back back" aria-label="Postcard back">
  <div class="family-photo" role="img" aria-label="Soft-focus photo of a smiling family of four"></div>

  <div class="about">
    <h2 class="about__title">Who We Are</h2>
    <p class="about__text">KRV Benefit Group is a HEALTH INSURANCE BROKERAGE focused on providing products for clients 65 and under as well as Medicare products for Seniors. We also offer Ancillary benefits such as critical illness, accident, life, dental and vision, small group products and investment products such as annuities.</p>
  </div>

  <div class="back-brand"><span class="brand-name">KRV</span></div>
  <p class="mail-address">1450 Maple Crest Dr.<br>Suite 210<br>Troy, MI 48083</p>
  <div class="stamp-box" aria-label="Stamp area"></div>

  <h2 class="back-title">The Year Ahead Summit</h2>
  <p class="back-teaser">Find out what 2020 has to offer</p>
  <p class="back-band">An opportunity to certify face to face<br>with MAPD carriers</p>

  <div class="back-contact">
    <p class="back-contact__label">CONFIRM YOUR ATTENDANCE</p>
    <p class="back-contact__phone">
      <svg class="icon" width="12" height="12" viewBox="0 0 16 16" aria-hidden="true"><circle cx="8" cy="8" r="7" fill="none" stroke="currentColor" stroke-width="1.4"/><path d="M5 4.5l1.5-.5 1 2-1 .8c.4 1 1 1.6 1.9 2l.8-1 2 1-.5 1.5c-2.8.2-5.6-2.7-5.7-5.8z" fill="currentColor"/></svg>
      (800) 555-0142
    </p>
    <ul class="back-contact__list">
      <li><svg class="icon" width="9" height="9" viewBox="0 0 16 16" aria-hidden="true"><circle cx="8" cy="8" r="7" fill="none" stroke="#1a1a1a" stroke-width="1.5"/><path d="M5 4.5l1.5-.5 1 2-1 .8c.4 1 1 1.6 1.9 2l.8-1 2 1-.5 1.5c-2.8.2-5.6-2.7-5.7-5.8z" fill="#1a1a1a"/></svg>(231) 555-0187</li>
      <li><svg class="icon" width="9" height="9" viewBox="0 0 16 16" aria-hidden="true"><rect x="4" y="1" width="8" height="5" fill="none" stroke="#1a1a1a" stroke-width="1.5"/><rect x="1" y="6" width="14" height="6" fill="#1a1a1a"/><rect x="4" y="10" width="8" height="5" fill="#fff" stroke="#1a1a1a" stroke-width="1.5"/></svg>(248) 555-0163</li>
      <li><svg class="icon" width="10" height="8" viewBox="0 0 16 12" aria-hidden="true"><rect x="1" y="1" width="14" height="10" fill="none" stroke="#1a1a1a" stroke-width="1.5"/><path d="M1 1l7 6 7-6" fill="none" stroke="#1a1a1a" stroke-width="1.5"/></svg>events@krvbenefit.com</li>
    </ul>
  </div>
</section>

</body>
</html>
```